Voltarey - Flyer design

Description -
Motorhome and Caravan EWOFs
Recreational Vehicles (such as caravans, motorhomes, RVs, Boats etc) and Relocatable buildings that can be connected to an electricity supply must be regularly checked for electrical safety. An EWOF needs to be issued every 4 years.
Pre-purchase house inspections
A pre-purchase electrical inspection prior to buying a home can be used to identify any dangerous and unsafe electrical parts of the installation that may be costly to repair once the property has been purchased. Giving you peace of mind when buying your new home.
High risk Electrical inspections
All Prescribed Electrical Work that falls under the High Risk category must be inspected by a Registered Electrical Inspector and have a Record of Inspection certificate issued.
Electric Vehicle Chargers
Any electrical vehicle charger that can be accessed by the public (ie in a non-domestic situation) must be periodically inspected and certified every 12 months.
General Electrical Services
Domestic and commercial - We do new builds, Renovations, Maintenance and more!
Dean Fowler - Electrician and Electrical Inspector
Ph - 0227839152
Dean@voltarey.co.nz
Auckland
------
I also want there to be a few symbols similar to the files I have attached.
The main areas that I am hoping to find work is with caravans/motohomes and EV car chargers so these symbols are quite important.
Thanks so much

```html
<!DOCTYPE html>
<html lang="en">
<head>
<meta charset="utf-8">
<title>Voltarey – Motorhome &amp; Caravan EWOF Flyer</title>
<link rel="stylesheet" href="https://fonts.googleapis.com/css2?family=Anton&family=Raleway:wght@500;600;700;800&family=Montserrat:wght@800;900&family=Dancing+Script:wght@700&display=swap">
<style>
  :root {
    --royal: #0b1f86;
    --midnight: #0a1150;
    --sun: #ffd500;
    --white: #ffffff;
    --silver: 226, 230, 236;
    --shade: 150, 158, 170;
    --overall: 52, 120, 205;
  }
  * { margin: 0; padding: 0; box-sizing: border-box; }
  html, body { width: 848px; height: 1200px; overflow: hidden; background: var(--royal); }
  .flyer { position: relative; width: 848px; height: 1200px; overflow: hidden; font-family: "Raleway", sans-serif; color: var(--white); }
  .backdrop, .headline { position: absolute; left: 0; top: 0; }
  .headline text { font-family: "Anton", sans-serif; }

  .placeholder { position: absolute; }
  .hero-vehicle { left: 84px; top: 236px; width: 612px; height: 388px;
    background: radial-gradient(ellipse 50% 50% at 50% 52%, rgba(var(--silver), .95) 0%, rgba(var(--silver), .85) 45%, rgba(var(--shade), .55) 72%, rgba(var(--shade), 0) 100%); }
  .hero-cable { left: 549px; top: 486px; width: 187px; height: 115px;
    background: radial-gradient(ellipse 50% 50% at 50% 50%, rgba(242,196,0,.95) 0%, rgba(242,196,0,.6) 50%, rgba(40,40,40,0) 100%); }
  .spark { left: 164px; top: 618px; width: 330px; height: 84px;
    background: radial-gradient(ellipse 50% 50% at 50% 50%, rgba(220,230,120,.5), rgba(10,17,80,0) 100%); }
  .mascot { left: 540px; top: 636px; width: 210px; height: 258px;
    background: radial-gradient(ellipse 45% 50% at 50% 50%, rgba(var(--overall), .9) 0%, rgba(var(--overall), .6) 55%, rgba(var(--overall), 0) 100%); }

  .services__title { position: absolute; left: 52px; top: 718px; width: 432px; color: var(--sun); font-weight: 700; font-size: 40px; text-align: center; line-height: 44px; letter-spacing: .4px; }
  .services__sub { position: absolute; left: 10px; top: 766px; width: 520px; font-weight: 500; font-size: 28px; text-align: center; line-height: 29px; }
  .service { position: absolute; left: 0; width: 530px; padding-left: 37px; }
  .service--risk { top: 828px; }
  .service--ev { top: 908px; }
  .service--general { top: 987px; }
  .service__tick { position: absolute; left: 14px; top: 4px; width: 17px; height: 17px; }
  .service__name { color: var(--sun); font-weight: 800; font-size: 23px; line-height: 25px; }
  .service__text { font-size: 13.6px; line-height: 16px; font-weight: 500; }

  .brand-row { position: absolute; left: 68px; top: 1054px; height: 58px; display: flex; align-items: center; }
  .brand { display: flex; align-items: center; gap: 7px; width: 158px; }
  .brand__mark { width: 12px; height: 12px; background: var(--sun); }
  .brand__name { color: var(--sun); font-weight: 700; font-size: 28px; }
  .brand-row .divider { width: 1.5px; height: 54px; background: var(--white); margin: 0 5px; }
  .service-icon { display: block; }
  .service-icon--pro { width: 54px; height: 54px; border-radius: 8px;
    background: radial-gradient(circle at 50% 45%, rgba(255,213,0,.85), rgba(255,213,0,.25) 70%, rgba(255,213,0,0) 100%); }
  .brand-row__caption { position: absolute; left: 68px; top: 1116px; font-weight: 700; font-size: 16px; letter-spacing: .2px; }

  .cycle-badge { position: absolute; left: 541px; top: 832px; width: 281px; height: 178px; border: 2.5px dashed var(--sun); }
  .cycle-badge__words { position: absolute; left: 15px; top: 62px; font-weight: 500; font-size: 37px; line-height: 35px; }
  .cycle-badge__num { position: absolute; left: 141px; top: -20px; font-family: "Montserrat", sans-serif; font-weight: 900; font-size: 206px; line-height: 1; }
  .cycle-badge__note { position: absolute; left: 24px; top: 134px; font-family: "Dancing Script", cursive; font-size: 23px; font-weight: 700; }

  .contact { position: absolute; left: 540px; top: 1026px; width: 300px; font-style: normal; }
  .contact__name { display: inline-block; margin-left: 25px; background: var(--white); color: var(--midnight); font-weight: 700; font-size: 13.5px; padding: 1px 4px; line-height: 15px; }
  .contact__line { display: flex; align-items: center; gap: 5px; }
  .contact__phone { color: var(--sun); font-family: "Montserrat", sans-serif; font-weight: 900; font-size: 36px; letter-spacing: .5px; line-height: 40px; }
  .contact__detail { font-size: 19.5px; font-weight: 500; line-height: 22px; }
  .contact svg { flex: none; }

  .footer-band { position: absolute; left: 0; top: 1148px; width: 848px; height: 52px; background: var(--white);
    color: var(--midnight); font-weight: 800; font-size: 37px; text-align: center; line-height: 52px; letter-spacing: .3px; }
</style>
</head>
<body>
<main class="flyer">
  <svg class="backdrop" width="848" height="1200" viewBox="0 0 848 1200" aria-hidden="true">
    <rect width="848" height="1200" fill="var(--royal)"/>
    <polygon points="354,0 624,0 0,475 0,354" fill="var(--sun)"/>
    <polygon points="0,575 280,612 848,592 848,653 0,722" fill="var(--sun)"/>
    <polygon points="0,722 848,653 848,1200 0,1200" fill="var(--midnight)"/>
  </svg>

  <div class="placeholder hero-vehicle" role="img" aria-label="Photo of a white motorhome"></div>
  <div class="placeholder hero-cable" role="img" aria-label="Photo of a stripped electrical cable"></div>
  <div class="placeholder spark" role="img" aria-label="Lightning glow beneath the motorhome"></div>

  <svg class="headline" width="848" height="560" viewBox="0 0 848 560" aria-label="Motorhome Caravan EWOF Electrical">
    <text x="44" y="242" textLength="666" lengthAdjust="spacingAndGlyphs" font-size="128" fill="var(--royal)" stroke="var(--white)" stroke-width="3" paint-order="stroke">CARAVAN EWOF</text>
    <text x="45" y="144" textLength="659" lengthAdjust="spacingAndGlyphs" font-size="134" fill="var(--white)">MOTORHOME</text>
    <text transform="translate(808,512) rotate(-90)" x="0" y="0" textLength="471" lengthAdjust="spacingAndGlyphs" font-size="118" fill="var(--royal)" stroke="var(--sun)" stroke-width="3">ELECTRICAL</text>
  </svg>

  <div class="placeholder mascot" role="img" aria-label="Cartoon electrician holding a screwdriver"></div>

  <section class="services">
    <h1 class="services__title">ELECTRICITY SUPPLY</h1>
    <p class="services__sub">SUCH AS CARAVANS, MOTORHOMES<br>RVS, BOATS ETC</p>
    <div class="service service--risk">
      <svg class="service__tick" viewBox="0 0 20 20"><circle cx="10" cy="10" r="10" fill="var(--sun)"/><path d="M5 10.5l3.2 3.2L15 6.5" stroke="var(--white)" stroke-width="2.6" fill="none" stroke-linecap="round"/></svg>
      <h2 class="service__name">HIGH RISK ELECTRICAL INSPECTIONS</h2>
      <p class="service__text">All Prescribed Electrical Work that falls under the High Risk category must<br>be inspected by a Registered Electrical Inspector and have a Record of<br>Inspection certificate issued.</p>
    </div>
    <div class="service service--ev">
      <svg class="service__tick" viewBox="0 0 20 20"><circle cx="10" cy="10" r="10" fill="var(--sun)"/><path d="M5 10.5l3.2 3.2L15 6.5" stroke="var(--white)" stroke-width="2.6" fill="none" stroke-linecap="round"/></svg>
      <h2 class="service__name">ELECTRIC VEHICLE CHARGERS</h2>
      <p class="service__text">Any electrical vehicle charger that can be accessed by the public (ie in a<br>non-domestic situation) must be periodically inspected and certified<br>every 12 months.</p>
    </div>
    <div class="service service--general">
      <svg class="service__tick" viewBox="0 0 20 20"><circle cx="10" cy="10" r="10" fill="var(--sun)"/><path d="M5 10.5l3.2 3.2L15 6.5" stroke="var(--white)" stroke-width="2.6" fill="none" stroke-linecap="round"/></svg>
      <h2 class="service__name">GENERAL ELECTRICAL SERVICES</h2>
      <p class="service__text">Domestic and commercial - We do new builds, Renovations, Maintenance<br>and more!</p>
    </div>
  </section>

  <div class="brand-row">
    <div class="brand"><span class="brand__mark"></span><span class="brand__name">Voltarey</span></div>
    <span class="divider"></span>
    <svg class="service-icon service-icon--ev" width="62" height="56" viewBox="0 0 62 56" role="img" aria-label="EV car charging icon">
      <path d="M46 10A25 25 0 1 0 52 40" fill="none" stroke="var(--sun)" stroke-width="3.5" stroke-linecap="round"/>
      <rect x="46" y="4" width="10" height="9" rx="2" fill="var(--sun)"/>
      <path d="M49 4V0M53 4V0" stroke="var(--sun)" stroke-width="2"/>
      <path d="M13 33l4-9c1-2 2-3 4-3h14c2 0 3 1 4 3l4 9v7H13z" fill="var(--sun)"/>
      <circle cx="20" cy="40" r="4" fill="var(--midnight)" stroke="var(--sun)" stroke-width="2"/>
      <circle cx="37" cy="40" r="4" fill="var(--midnight)" stroke="var(--sun)" stroke-width="2"/>
      <path d="M30 24l-5 7h4l-2 6 6-8h-4z" fill="var(--midnight)"/>
    </svg>
    <span class="divider"></span>
    <div class="service-icon service-icon--pro" role="img" aria-label="Electrician with test meter icon"></div>
    <span class="divider"></span>
    <svg class="service-icon service-icon--caravan" width="84" height="50" viewBox="0 0 84 50" role="img" aria-label="Caravan icon">
      <path d="M14 36V12c0-4 3-7 7-7h50c4 0 7 3 7 7v24z" fill="none" stroke="var(--sun)" stroke-width="3" stroke-linejoin="round"/>
      <rect x="22" y="12" width="26" height="12" rx="2" fill="none" stroke="var(--sun)" stroke-width="2.5"/>
      <path d="M35 12v12" stroke="var(--sun)" stroke-width="2"/>
      <rect x="56" y="12" width="13" height="24" rx="1.5" fill="none" stroke="var(--sun)" stroke-width="2.5"/>
      <path d="M14 36H2M4 36v-4" stroke="var(--sun)" stroke-width="3" stroke-linecap="round"/>
      <circle cx="44" cy="38" r="6" fill="var(--midnight)" stroke="var(--sun)" stroke-width="3"/>
      <path d="M78 30h4" stroke="var(--sun)" stroke-width="3"/>
    </svg>
  </div>
  <p class="brand-row__caption">CARAVANS/MOTOHOMES &amp; EV CAR CHARGERS</p>

  <div class="cycle-badge">
    <p class="cycle-badge__words">EVERY<br>YEARS</p>
    <p class="cycle-badge__num">4</p>
    <p class="cycle-badge__note">A quality certificate</p>
  </div>

  <address class="contact">
    <span class="contact__name">DEAN FOWLER</span>
    <p class="contact__line">
      <svg width="20" height="20" viewBox="0 0 20 20"><circle cx="10" cy="10" r="10" fill="var(--sun)"/><path d="M6.5 5.5l2 2-1 1.4c.7 1.5 1.8 2.6 3.3 3.3l1.4-1 2 2-1.2 1.3c-3.6-.6-7-4-7.6-7.6z" fill="var(--midnight)"/></svg>
      <span class="contact__phone">0227839152</span>
    </p>
    <p class="contact__line">
      <svg width="20" height="14" viewBox="0 0 20 14"><rect width="20" height="14" rx="1.5" fill="var(--white)"/><path d="M1 1l9 7 9-7" stroke="var(--midnight)" stroke-width="1.6" fill="none"/></svg>
      <span class="contact__detail">Dean@voltarey.co.nz</span>
    </p>
    <p class="contact__line">
      <svg width="20" height="22" viewBox="0 0 20 22"><path d="M10 1a6 6 0 0 1 6 6c0 4.5-6 10-6 10S4 11.5 4 7a6 6 0 0 1 6-6z" fill="none" stroke="var(--white)" stroke-width="1.8"/><circle cx="10" cy="7" r="2" fill="var(--white)"/><ellipse cx="10" cy="20" rx="5" ry="1.3" fill="none" stroke="var(--white)" stroke-width="1.2"/></svg>
      <span class="contact__detail">Auckland</span>
    </p>
  </address>

  <footer class="footer-band">ELECTRICIAN &amp; ELECTRICAL INSPECTOR</footer>
</main>
</body>
</html>
```